Magnetic Business card Design do a service provider

Hi,

The company aim is to provide all service needs under one roof. However, at the moment there is only Accounting, Electrical and IT branches. There will be more services coming onboard in the future.

I already have a logo designed (Company name is already part of the logo), I now need a magnetic business card designed.

The business card will contain the following:

- Company Logo
- Contact#
- E-mail
- enough space to add website URL (for future)
Updates

Project Deadline Extended Reason: HI All,The deadline has been extended due to not having enough time to review an overwhelming number of designs that has been submitted by lots of designers.I will be uploading a draft of designs that i have in mind.Thanks. Added Friday, January 22, 2016

Target Market(s)

Residential, Home-based Businesses, Small and Medium businesses

Industry/Entity Type

Business

Contact Information for Business Card

Contact#: 0491 738 520
E-mail: service@brightlanetrades.net.au

Font styles to use
Decorative
Script

Requirements
Must have
• Round edges
• Some form of logo incorporation as a background

```html
<!DOCTYPE html>
<html lang="en">
<head>
<meta charset="utf-8">
<title>Brightlane Trades – Magnetic Business Card</title>
<link rel="stylesheet" href="https://fonts.googleapis.com/css2?family=Kalam:wght@400;700&display=swap">
<style>
  :root {
    --backdrop: #d9d9d9;
    --card-blue: #0b5aa6;
    --card-blue-light: #1b6fbe;
    --card-blue-deep: #084a8c;
    --ink-white: #ffffff;
    --ink-soft: #eaf2fb;
  }
  * { margin: 0; padding: 0; box-sizing: border-box; }
  html, body {
    width: 1200px;
    height: 913px;
    overflow: hidden;
    background: var(--backdrop);
  }
  .stage {
    width: 1200px;
    height: 913px;
    display: flex;
    align-items: center;
    justify-content: center;
  }
  .business-card {
    position: relative;
    width: 840px;
    height: 500px;
    border-radius: 44px;
    background: linear-gradient(135deg, var(--card-blue-light) 0%, var(--card-blue) 50%, var(--card-blue-deep) 100%);
    box-shadow: 0 18px 40px rgba(0, 0, 0, 0.25);
    color: var(--ink-white);
    font-family: "Kalam", cursive;
  }
  .brand {
    position: absolute;
    left: 0;
    right: 0;
    top: 150px;
    display: flex;
    align-items: center;
    justify-content: center;
    gap: 16px;
  }
  .brand-dot {
    width: 34px;
    height: 34px;
    border-radius: 50%;
    background: var(--ink-white);
  }
  .brand-name {
    font-family: "Kalam", cursive;
    font-weight: 400;
    font-size: 46px;
    line-height: 1;
    color: var(--ink-white);
  }
  .contact {
    position: absolute;
    left: 0;
    right: 0;
    top: 285px;
    text-align: center;
  }
  .contact-phone {
    font-weight: 700;
    font-size: 30px;
    letter-spacing: 2px;
    line-height: 1.2;
  }
  .contact-email,
  .contact-web {
    font-weight: 400;
    font-size: 24px;
    line-height: 1.35;
    color: var(--ink-soft);
  }
</style>
</head>
<body>
  <main class="stage">
    <section class="business-card" aria-label="Brightlane Trades business card">
      <div class="brand">
        <span class="brand-dot" aria-hidden="true"></span>
        <span class="brand-name">Brightlane Trades</span>
      </div>
      <div class="contact">
        <p class="contact-phone">0491 738 520</p>
        <p class="contact-email">service@brightlanetrades.net.au</p>
        <p class="contact-web">www.brightlanetrades.net.au</p>
      </div>
    </section>
  </main>
</body>
</html>
```